Finance Broker helping people meet their personal and business goals

New business card design,
1st look at the old business card so this makes sense.
I DON'T want:
the subtext "For all your Rural and Commercial Finance".
I DON'T want the: "and Management Consultant" words
I DON'T want the old phone: 07 48213957
I DON'T want the fax number: 07 45826031
I DON'T want the email address: tallowcreek@brightlink.com.au
I DON'T want the flower
What I DO want
I DO want the mobile 0451 836 209 (in larger text)
I DO want:
My name: Dennis Harwell-Lowe
I DO want: Australian Credit Licence 529164 (Tallow Creek Pty Ltd)
I DO want: Principal Finance Broker
I DO want new email: dennis@plotnextstep.com.au
I DO want address: PO Box 928, Tully Qld 4854
I DO want the existing logo (PNS on existing card)

Target Market(s)

Business Borrowers, Home Purchasers, and People wanting to finance cars and plant and equipment

Industry/Entity Type

Financial Service

Contact Information for Business Card

See project description

Font styles to use
Serif

Colors

Designer to choose colors to be used in the design.

Requirements
Must have
• See project description
Nice to have
• Black and Yellow colours
Should not have
• See project description

```html
<!DOCTYPE html>
<html lang="en">
<head>
<meta charset="utf-8">
<title>Plot Next Step – Business Card</title>
<link rel="stylesheet" href="https://fonts.googleapis.com/css2?family=Tinos:wght@400;700&family=Jost:wght@400&display=swap">
<style>
  :root {
    --backdrop: #b9b9b9;
    --ink-dark: #2a2f2d;
    --lime: #dbe35a;
    --paper: #ffffff;
    --text: #222222;
    --rule: #333333;
  }
  * { margin: 0; padding: 0; box-sizing: border-box; }
  html, body { width: 1200px; height: 930px; overflow: hidden; }
  body {
    background: var(--backdrop);
    font-family: "Tinos", "Times New Roman", serif;
    position: relative;
  }
  .card {
    position: absolute;
    width: 560px;
    height: 320px;
    border-radius: 22px;
    overflow: hidden;
    box-shadow: 0 6px 14px rgba(0,0,0,0.25);
  }
  /* Front */
  .card--front { left: 90px; top: 110px; background: var(--ink-dark); }
  .card--front .brand { position: absolute; left: 120px; top: 132px; }
  .brand__row { display: flex; align-items: center; gap: 12px; }
  .brand__name {
    font-family: "Tinos", serif; font-weight: 700; font-size: 30px; color: var(--lime);
  }
  .brand__dot { width: 26px; height: 26px; border-radius: 50%; background: var(--lime); }
  .brand__tagline {
    font-family: "Jost", sans-serif; font-size: 13px; letter-spacing: 0.6px;
    color: var(--paper); margin-top: 4px;
  }
  /* Back */
  .card--back { left: 550px; top: 480px; background: var(--paper); }
  .card--back .brand { position: absolute; left: 28px; top: 40px; }
  .card--back .brand__name { color: var(--ink-dark); font-size: 24px; }
  .card--back .brand__dot { width: 22px; height: 22px; }
  .card--back .brand__tagline { color: #b8c23a; font-size: 11px; }
  .holder { position: absolute; right: 22px; top: 98px; text-align: right; color: var(--text); }
  .holder__name { font-size: 24px; text-transform: uppercase; letter-spacing: 0.3px; }
  .holder__role, .holder__licence { font-size: 15px; line-height: 1.3; }
  .holder__role { margin-top: 6px; }
  .rule { position: absolute; height: 1px; background: var(--rule); }
  .rule--name { left: 230px; right: 0; top: 130px; }
  .rule--long { left: 0; width: 230px; top: 180px; }
  .contact { position: absolute; left: 28px; top: 222px; font-size: 16px; color: var(--text); line-height: 1.3; }
  .bands { position: absolute; left: 0; top: 0; }
  .phone {
    position: absolute; right: 22px; top: 268px; font-weight: 700; font-size: 26px;
    color: var(--lime); letter-spacing: 0.5px;
  }
</style>
</head>
<body>
  <section class="card card--front" aria-label="Card front">
    <div class="brand">
      <div class="brand__row">
        <span class="brand__name">Plot Next Step</span>
        <span class="brand__dot"></span>
      </div>
      <p class="brand__tagline">A Member of the Tallow Creek Group</p>
    </div>
  </section>

  <section class="card card--back" aria-label="Card back">
    <svg class="bands" width="560" height="320" viewBox="0 0 560 320" aria-hidden="true">
      <polygon points="0,306 380,284 384,320 0,320" fill="var(--lime)"/>
      <polygon points="372,248 560,248 560,320 380,320" fill="var(--ink-dark)"/>
    </svg>
    <div class="brand">
      <div class="brand__row">
        <span class="brand__name">Plot Next Step</span>
        <span class="brand__dot"></span>
      </div>
      <p class="brand__tagline">A Member of the Tallow Creek Group</p>
    </div>
    <div class="holder">
      <p class="holder__name">Dennis Harwell-Lowe</p>
      <p class="holder__role">Principal Finance Broker</p>
      <p class="holder__licence">Australian Credit Licence 529164</p>
    </div>
    <div class="rule rule--name"></div>
    <div class="rule rule--long"></div>
    <div class="contact">
      <p>dennis@plotnextstep.com.au</p>
      <p>PO Box 928, Tully Qld 4854</p>
    </div>
    <p class="phone">0451 836 209</p>
  </section>
</body>
</html>
```